Block makes the buck for writing

We need a notepad in DIN A4 format which we can give to our customers at events. We, TAVORIK, are active in the field of safe electrical engineering and offer software, hardware, academia and consulting in this field. With our software can be z. For example, you can quickly and easily inventory and document all equipment and equipment. Every tool must be checked in Germany and the test repeated at regular intervals. The appropriate test specifications are stored in our software. In addition to the software, we also offer measuring and testing equipment. In our academy, we also offer seminars on various areas of safe electrical engineering. Our consulting advises companies on the establishment of a legally compliant company organization. If necessary, our experts also take on the temporary function of external responsible electrician. So we offer an all-round package concerning safe electrical engineering. TAVORIK makes working with electricity safe. Every year we offer an event with different workshops. There the users of our software are invited. You can exchange ideas with our lecturers and experts and exchange experiences and tips with each other. For this event we need a writing pad where participants can take their notes throughout the day. In addition, the block should also be used by customers. But it would be nice if he had a special feature / a special feature by which he is particularly happy to use. As basic the block should be branded with our logo and our URL (tavorik.de).

```html
<!DOCTYPE html>
<html lang="de">
<head>
<meta charset="utf-8">
<title>TAVORIK Notizblock</title>
<link rel="stylesheet" href="https://fonts.googleapis.com/css2?family=Barlow+Semi+Condensed:wght@500;600&family=Barlow:wght@500;700&display=swap">
<style>
  :root {
    --backdrop: #d9dadd;
    --cover-light: #73746d;
    --cover-dark: #5b5c56;
    --paper: #ffffff;
    --ink: #55564f;
    --ink-soft: #6b6c66;
    --rule: #dcdddd;
    --accent: #f5a31c;
    --white: #ffffff;
  }
  html, body {
    margin: 0;
    padding: 0;
    width: 1200px;
    height: 870px;
    overflow: hidden;
    background: var(--backdrop);
  }
  .sheet {
    position: absolute;
    top: 92px;
    width: 502px;
    height: 706px;
  }
  .cover {
    left: 69px;
    background: linear-gradient(225deg, var(--cover-light) 0%, var(--cover-dark) 100%);
  }
  .notepage {
    left: 631px;
    background: var(--paper);
  }
  .brand {
    position: absolute;
    display: flex;
    align-items: center;
    gap: 12px;
  }
  .brand-name {
    font-family: "Barlow Semi Condensed", sans-serif;
    font-weight: 600;
    font-size: 35px;
    line-height: 1;
    letter-spacing: 0.2px;
  }
  .brand-dot {
    width: 42px;
    height: 42px;
    border-radius: 50%;
    background: var(--accent);
    flex: none;
  }
  .cover .brand {
    right: 67px;
    bottom: 42px;
  }
  .cover .brand-name { color: var(--white); }

  .notepage .brand {
    right: 41px;
    top: 66px;
  }
  .notepage .brand-name { color: var(--ink); }
  .tagline {
    position: absolute;
    right: 96px;
    top: 112px;
    font-family: "Barlow", sans-serif;
    font-weight: 700;
    font-size: 9.5px;
    color: var(--ink);
    white-space: nowrap;
  }
  .date-field {
    position: absolute;
    left: 39px;
    top: 107px;
    display: flex;
    align-items: baseline;
    gap: 7px;
    font-family: "Barlow", sans-serif;
    font-weight: 500;
    font-size: 12.5px;
    color: var(--ink);
  }
  .date-line {
    width: 100px;
    border-bottom: 1px solid var(--rule);
  }
  .rules {
    position: absolute;
    left: 0;
    top: 0;
  }
  .web {
    position: absolute;
    right: 41px;
    top: 664px;
    display: flex;
    align-items: center;
    gap: 8px;
    font-family: "Barlow", sans-serif;
    font-size: 11.5px;
    color: var(--ink);
  }
  .web-mark {
    width: 6px;
    height: 6px;
    background: var(--accent);
  }
  .web-name { font-weight: 700; }
  .web-tld { font-weight: 500; color: var(--ink-soft); }
</style>
</head>
<body>
  <section class="sheet cover" aria-label="Umschlag">
    <div class="brand">
      <span class="brand-name">TAVORIK</span>
      <span class="brand-dot"></span>
    </div>
  </section>

  <section class="sheet notepage" aria-label="Notizseite">
    <div class="date-field"><span>Date:</span><span class="date-line"></span></div>
    <div class="brand">
      <span class="brand-name">TAVORIK</span>
      <span class="brand-dot"></span>
    </div>
    <div class="tagline">verlässlich | normgerecht | vollständig</div>

    <svg class="rules" width="502" height="706" viewBox="0 0 502 706" aria-hidden="true">
      <g stroke="var(--rule)" stroke-width="1">
        <line x1="41" x2="461" y1="173" y2="173"/>
        <line x1="41" x2="461" y1="196.8" y2="196.8"/>
        <line x1="41" x2="461" y1="220.6" y2="220.6"/>
        <line x1="41" x2="461" y1="244.4" y2="244.4"/>
        <line x1="41" x2="461" y1="268.2" y2="268.2"/>
        <line x1="41" x2="461" y1="292" y2="292"/>
        <line x1="41" x2="461" y1="315.8" y2="315.8"/>
        <line x1="41" x2="461" y1="339.6" y2="339.6"/>
        <line x1="41" x2="461" y1="363.4" y2="363.4"/>
        <line x1="41" x2="461" y1="387.2" y2="387.2"/>
        <line x1="41" x2="461" y1="411" y2="411"/>
        <line x1="41" x2="461" y1="434.8" y2="434.8"/>
        <line x1="41" x2="461" y1="458.6" y2="458.6"/>
        <line x1="41" x2="461" y1="482.4" y2="482.4"/>
        <line x1="41" x2="461" y1="506.2" y2="506.2"/>
        <line x1="41" x2="461" y1="530" y2="530"/>
        <line x1="41" x2="461" y1="553.8" y2="553.8"/>
        <line x1="41" x2="461" y1="577.6" y2="577.6"/>
        <line x1="41" x2="461" y1="601.4" y2="601.4"/>
        <line x1="41" x2="461" y1="625.2" y2="625.2"/>
        <line x1="41" x2="461" y1="649" y2="649"/>
        <line x1="41" x2="379" y1="672.8" y2="672.8"/>
      </g>
    </svg>

    <div class="web">
      <span class="web-mark"></span>
      <span><span class="web-name">tavorik</span><span class="web-tld">.de</span></span>
    </div>
  </section>
</body>
</html>
```